Stationary for a property rental company
Glenbrook Rentals
Stationary for a property rental company - Real Estate
Creative Brief
Simple
Marla Pike
Owner
PO Box 7413 Ashford Falls, VT 05199
marla@glenbrookrentals-example.net
www.glenbrookrentals-example.net
Please use similar colors that are found in the Logo.
Use emblem for the back of the card

```html
<!DOCTYPE html>
<html lang="en">
<head>
<meta charset="utf-8">
<title>Glenbrook Rentals – Business Card</title>
<link rel="stylesheet" href="https://fonts.googleapis.com/css2?family=Crimson+Text:wght@400;700&display=swap">
<style>
  :root {
    --stage: #e9ecee;
    --card-white: #ffffff;
    --slate-blue: #4f8099;
    --slate-deep: #2f5d78;
    --steel-light: #6d9cb4;
    --ink: #3b3b3b;
    --muted: #777c80;
    --rule: #9aa3a8;
  }
  * { box-sizing: border-box; margin: 0; padding: 0; }
  html, body { width: 1200px; height: 901px; overflow: hidden; }
  body {
    background: var(--stage);
    font-family: "Crimson Text", Georgia, serif;
    position: relative;
  }
  .card {
    position: absolute;
    top: 296px;
    width: 540px;
    height: 309px;
    border-radius: 22px;
    overflow: hidden;
    box-shadow: 0 6px 18px rgba(0,0,0,0.18);
  }
  /* Back side */
  .card-back {
    left: 40px;
    background: linear-gradient(160deg, var(--steel-light) 0%, var(--slate-blue) 45%, var(--slate-deep) 100%);
    display: flex;
    flex-direction: column;
    align-items: center;
    justify-content: center;
    gap: 14px;
  }
  .emblem-circle {
    width: 44px; height: 44px;
    border: 3px solid rgba(255,255,255,0.9);
    border-radius: 50%;
  }
  .emblem-name {
    color: #ffffff;
    font-weight: 700;
    font-size: 30px;
    letter-spacing: 3px;
    text-transform: uppercase;
  }
  /* Front side */
  .card-front {
    left: 620px;
    background: var(--card-white);
  }
  .brand {
    position: absolute;
    top: 62px; left: 0; right: 0;
    display: flex;
    align-items: center;
    justify-content: center;
    gap: 12px;
  }
  .brand-mark {
    width: 28px; height: 28px;
    background: var(--slate-blue);
    border-radius: 50%;
  }
  .brand-name {
    color: var(--slate-deep);
    font-weight: 700;
    font-size: 30px;
    letter-spacing: 2px;
    text-transform: uppercase;
  }
  .person {
    position: absolute;
    top: 168px; left: 70px;
    width: 150px;
    text-align: right;
  }
  .person-name {
    color: var(--slate-blue);
    font-weight: 700;
    font-size: 19px;
    line-height: 1.1;
  }
  .person-role {
    color: var(--muted);
    font-size: 14px;
    margin-top: 2px;
  }
  .divider {
    position: absolute;
    top: 166px; left: 236px;
    width: 1px; height: 112px;
    background: var(--rule);
  }
  .contact {
    position: absolute;
    top: 164px; left: 250px;
    color: var(--ink);
    font-size: 13.5px;
    line-height: 1.3;
  }
  .address { margin-bottom: 6px; }
  .contact-line {
    display: flex;
    align-items: center;
    gap: 6px;
    height: 18px;
  }
  .contact-line svg { width: 12px; height: 12px; flex: none; }
</style>
</head>
<body>

  <section class="card card-back" aria-label="Card back">
    <div class="emblem-circle"></div>
    <div class="emblem-name">Glenbrook Rentals</div>
  </section>

  <section class="card card-front" aria-label="Card front">
    <div class="brand">
      <div class="brand-mark"></div>
      <div class="brand-name">Glenbrook Rentals</div>
    </div>

    <div class="person">
      <div class="person-name">Marla Pike</div>
      <div class="person-role">Owner</div>
    </div>

    <div class="divider"></div>

    <div class="contact">
      <div class="address">PO Box 7413<br>Ashford Falls, VT 05199</div>
      <div class="contact-line">
        <svg viewBox="0 0 12 12" aria-hidden="true"><rect width="12" height="12" rx="2" fill="#4f8099"/><path d="M3.5 2.5l1.6 1.6-.9.9a5 5 0 0 0 2.8 2.8l.9-.9 1.6 1.6-1 1C6 9.5 2.5 6 2.5 3.5z" fill="#fff"/></svg>
        <span>802.555.0178</span>
      </div>
      <div class="contact-line">
        <svg viewBox="0 0 12 12" aria-hidden="true"><rect width="12" height="12" rx="2" fill="#4f8099"/><rect x="2.5" y="3.5" width="7" height="5" fill="none" stroke="#fff" stroke-width="1"/><path d="M2.5 3.5L6 6.3l3.5-2.8" fill="none" stroke="#fff" stroke-width="1"/></svg>
        <span>marla@glenbrookrentals-example.net</span>
      </div>
      <div class="contact-line">
        <svg viewBox="0 0 12 12" aria-hidden="true"><circle cx="6" cy="6" r="6" fill="#4f8099"/><circle cx="6" cy="6" r="3.6" fill="none" stroke="#fff" stroke-width="0.9"/><path d="M2.4 6h7.2M6 2.4c-1.6 2-1.6 5.2 0 7.2M6 2.4c1.6 2 1.6 5.2 0 7.2" fill="none" stroke="#fff" stroke-width="0.8"/></svg>
        <span>www.glenbrookrentals-example.net</span>
      </div>
    </div>
  </section>

</body>
</html>
```